Coffeeshop menu for filter tip

We want to have a cannabis (coffeeshop) menu in the size 25mm wide x 60mm wide. Some examples attached.

it must have the following text:
Menu

WEED p/g
Velotrine €16
Cinderfox €14
Tide Rambler €14
Marigolden €16
Grand Pelican €14
Copper Comet €14

HASH p/g
Baltic Ember €12
Harbor Velvet€11
Plum Rova €14
Dusk Maple €10

Target Market(s)

tourist in Amsterdam

Requirements
Nice to have
• cannabis sign leaf
• No Cigarettes allowed symbol

```html
<!DOCTYPE html>
<html lang="en">
<head>
<meta charset="utf-8">
<title>Amsterdam Menu</title>
<link href="https://fonts.googleapis.com/css2?family=Cinzel:wght@400;500&family=Alegreya:wght@400;700&display=swap" rel="stylesheet">
<style>
  :root {
    --bg-dark: #3a0a0c;
    --bg-mid: #540e10;
    --bg-warm: #7b3a2a;
    --frame: #8a4a22;
    --rule: #8a4a22;
    --rule-soft: #5e1a14;
    --text: #ffffff;
    --gold: #f2a93b;
    --leaf-faint: rgba(190, 130, 130, 0.45);
    --no-red: #e8222a;
    --filter-tan: #b08560;
  }
  * { margin: 0; padding: 0; box-sizing: border-box; }
  html, body { width: 1200px; height: 2872px; overflow: hidden; }
  body { background: var(--bg-dark); }
  .menu-card {
    position: relative;
    width: 1200px;
    height: 2872px;
    background: linear-gradient(30deg, var(--bg-warm) 0%, #5f1718 32%, var(--bg-mid) 60%, var(--bg-dark) 100%);
    color: var(--text);
    overflow: hidden;
  }
  .frame {
    position: absolute;
    left: 25px; top: 31px; width: 1150px; height: 2812px;
    border: 7px solid var(--frame);
  }
  .title {
    position: absolute;
    left: 0; width: 100%;
    text-align: center;
    font-family: "Cinzel", serif;
    font-weight: 400;
    font-size: 116px;
    line-height: 1;
    letter-spacing: 2px;
  }
  .title--city { top: 94px; }
  .title--menu { top: 290px; }
  .title-leaf {
    position: absolute;
    top: 89px; width: 106px; height: 106px;
    border-radius: 50%;
    background: radial-gradient(circle, var(--gold) 0%, rgba(242,169,59,0.6) 45%, rgba(242,169,59,0) 72%);
  }
  .title-leaf--left { left: 98px; }
  .title-leaf--right { left: 1006px; }
  .rule {
    position: absolute;
    left: 65px; width: 1048px;
    background: var(--rule);
  }
  .rule--title { top: 403px; height: 3px; }
  .rule--weed { top: 675px; height: 2px; background: var(--rule-soft); }
  .rule--hash { top: 1897px; height: 3px; }
  .leaf-decor {
    position: absolute;
    left: 357px; top: 1087px; width: 702px; height: 770px;
    border-radius: 50% 50% 45% 45%;
    background: radial-gradient(ellipse at 50% 55%, var(--leaf-faint) 0%, rgba(190,130,130,0.2) 45%, rgba(190,130,130,0) 70%);
  }
  .section-head {
    position: absolute;
    font-family: "Alegreya", serif;
    font-weight: 400;
    font-size: 86px;
    line-height: 1;
  }
  .item {
    position: absolute;
    font-family: "Alegreya", serif;
    font-weight: 700;
    font-size: 72px;
    line-height: 1;
    letter-spacing: 1px;
  }
  .item--name { left: 84px; }
  .item--price { text-align: right; }
  .no-smoking {
    position: absolute;
    left: 150px; top: 2640px;
  }
</style>
</head>
<body>
<main class="menu-card">
  <div class="frame"></div>

  <div class="title-leaf title-leaf--left" role="img" aria-label="Small golden cannabis leaf"></div>
  <h1 class="title title--city">AMSTERDAM</h1>
  <div class="title-leaf title-leaf--right" role="img" aria-label="Small golden cannabis leaf"></div>
  <h2 class="title title--menu">MENU</h2>
  <div class="rule rule--title"></div>

  <div class="leaf-decor" role="img" aria-label="Large faint cannabis leaf in the background"></div>

  <section class="menu-section menu-section--weed">
    <div class="section-head" style="left:98px; top:578px;">WEED</div>
    <div class="section-head" style="left:900px; top:578px;">p/g</div>
    <div class="rule rule--weed"></div>

    <div class="item item--name" style="top:740px;">Velotrine</div>
    <div class="item item--price" style="right:174px; top:740px;">€16</div>
    <div class="item item--name" style="top:901px;">Cinderfox</div>
    <div class="item item--price" style="right:182px; top:901px;">€14</div>
    <div class="item item--name" style="top:1063px;">Tide Rambler</div>
    <div class="item item--price" style="right:182px; top:1063px;">€14</div>
    <div class="item item--name" style="top:1225px;">Marigolden</div>
    <div class="item item--price" style="right:188px; top:1225px;">€16</div>
    <div class="item item--name" style="top:1386px;">Grand Pelican</div>
    <div class="item item--price" style="right:182px; top:1386px;">€14</div>
    <div class="item item--name" style="top:1548px;">Copper Comet</div>
    <div class="item item--price" style="right:172px; top:1548px;">€14</div>
  </section>

  <section class="menu-section menu-section--hash">
    <div class="section-head" style="left:84px; top:1799px;">HASH</div>
    <div class="section-head" style="left:914px; top:1799px;">p/g</div>
    <div class="rule rule--hash"></div>

    <div class="item item--name" style="top:1972px;">Baltic Ember</div>
    <div class="item item--price" style="right:152px; top:1972px;">€12</div>
    <div class="item item--name" style="top:2133px;">Harbor Velvet</div>
    <div class="item item--price" style="right:148px; top:2133px;">€11</div>
    <div class="item item--name" style="top:2295px;">Plum Rova</div>
    <div class="item item--price" style="right:143px; top:2295px;">€14</div>
    <div class="item item--name" style="top:2457px;">Dusk Maple</div>
    <div class="item item--price" style="right:143px; top:2457px;">€10</div>
  </section>

  <svg class="no-smoking" width="260" height="150" viewBox="0 0 260 150" role="img" aria-label="No smoking">
    <rect x="3" y="71" width="46" height="22" fill="var(--filter-tan)"/>
    <rect x="49" y="71" width="117" height="22" fill="#ffffff"/>
    <rect x="166" y="71" width="6" height="22" fill="#222222"/>
    <circle cx="86" cy="77" r="60" fill="none" stroke="var(--no-red)" stroke-width="10"/>
    <line x1="44" y1="119" x2="128" y2="35" stroke="var(--no-red)" stroke-width="10"/>
    <path d="M178 66 C170 40 200 30 230 20 C240 16 248 10 250 4 C252 30 220 40 200 48 C190 52 182 58 178 66 Z" fill="none" stroke="#ffffff" stroke-width="3"/>
  </svg>
</main>
</body>
</html>
```